New Business Card Design Project

I need a meaningful new business card. Therefore, the website should convey growth, joy, uniqueness, workout and a bit of luxury.
Color scheme should be petrol, gold and matching colors.

```html
<!DOCTYPE html>
<html lang="en">
<head>
<meta charset="utf-8">
<title>Kernwerk Studio – Business Card</title>
<link rel="stylesheet" href="https://fonts.googleapis.com/css2?family=Great+Vibes&family=Open+Sans:wght@400;600&display=swap">
<style>
  :root {
    --backdrop: #1f4a52;
    --backdrop-deep: #163a41;
    --card: #161616;
    --gold: #c99a2e;
    --gold-light: #e8c45a;
    --gold-deep: #9a6c16;
    --ink: #f4f4f2;
    --emboss: #2b2b2b;
  }
  * { margin: 0; padding: 0; box-sizing: border-box; }
  html, body { width: 1200px; height: 801px; overflow: hidden; }
  body {
    background: radial-gradient(ellipse at center, var(--backdrop) 0%, var(--backdrop-deep) 100%);
    font-family: "Open Sans", Arial, sans-serif;
    display: flex;
    align-items: center;
    justify-content: center;
    gap: 48px;
  }
  .card {
    position: relative;
    width: 540px;
    height: 310px;
    background: var(--card);
    border-radius: 18px;
    box-shadow: 0 0 0 3px var(--gold), 0 18px 40px rgba(0,0,0,.4);
    overflow: hidden;
  }
  .card__corner-bar {
    position: absolute;
    top: 0; right: 26px;
    width: 36px; height: 14px;
    background: linear-gradient(90deg, var(--gold-deep), var(--gold-light), var(--gold));
  }
  .card__name {
    position: absolute;
    top: 24px; right: 30px;
    font-family: "Great Vibes", cursive;
    font-size: 34px;
    color: var(--gold);
    line-height: 1;
  }
  .card__role {
    position: absolute;
    top: 64px; right: 30px;
    font-size: 15px;
    color: var(--ink);
  }
  .card__emboss-name {
    position: absolute;
    top: 104px; right: 30px;
    font-size: 30px;
    font-weight: 600;
    color: var(--emboss);
    white-space: nowrap;
  }
  .brand {
    display: flex;
    align-items: center;
    gap: 10px;
    color: var(--gold);
    font-weight: 600;
    white-space: nowrap;
  }
  .brand__dot {
    border: 2px solid var(--gold);
    border-radius: 50%;
    flex: none;
  }
  .card--front .brand {
    position: absolute;
    top: 150px; left: 30px;
    font-size: 24px;
  }
  .card--front .brand__dot { width: 20px; height: 20px; }
  .contact {
    position: absolute;
    left: 30px; bottom: 24px;
    list-style: none;
    color: var(--ink);
    font-size: 15px;
    line-height: 1.6;
  }
  .contact li { display: flex; align-items: center; gap: 9px; }
  .contact svg { width: 14px; height: 14px; fill: none; stroke: var(--gold); stroke-width: 2; }
  .social {
    position: absolute;
    right: 30px; bottom: 28px;
    display: flex;
    align-items: center;
    gap: 9px;
    color: var(--ink);
    font-size: 15px;
  }
  .social__dot {
    width: 13px; height: 13px;
    border: 2px solid var(--gold);
    border-radius: 50%;
  }
  .card--back {
    display: flex;
    align-items: center;
    justify-content: center;
  }
  .card--back .brand { font-size: 46px; gap: 16px; }
  .card--back .brand__dot { width: 34px; height: 34px; border-width: 3px; }
</style>
</head>
<body>

  <section class="card card--front" aria-label="Business card front">
    <span class="card__corner-bar"></span>
    <p class="card__name">Marlene Vossberg</p>
    <p class="card__role">Pilates Studio Trainer</p>
    <p class="card__emboss-name" aria-hidden="true">Kernwerk Studio</p>

    <div class="brand">
      <span class="brand__dot"></span>
      <span class="brand__name">Kernwerk Studio</span>
    </div>

    <ul class="contact">
      <li>
        <svg viewBox="0 0 16 16"><path d="M4 2l2.5 3-1.5 2a8 8 0 004 4l2-1.5 3 2.5-1.5 2C7 14 2 9 2 3.5z"/></svg>
        49 160 5550184
      </li>
      <li>
        <svg viewBox="0 0 16 16"><rect x="2" y="4" width="12" height="9" rx="1"/><path d="M2 4l6 5 6-5"/></svg>
        info@studio-beispielhof.de
      </li>
      <li>
        <svg viewBox="0 0 16 16"><circle cx="8" cy="8" r="6"/><path d="M2 8h12M8 2c2.5 3 2.5 9 0 12M8 2c-2.5 3-2.5 9 0 12"/></svg>
        Studio-beispielhof.de
      </li>
    </ul>

    <div class="social">
      <span class="social__handle">kernwerk_studiopraxis</span>
      <span class="social__dot"></span>
    </div>
  </section>

  <section class="card card--back" aria-label="Business card back">
    <div class="brand">
      <span class="brand__dot"></span>
      <span class="brand__name">Kernwerk Studio</span>
    </div>
  </section>

</body>
</html>
```